Borrowdale Equity Business Card

Looking for a design for our business cards. Need to look corporate and outstanding. I have enclosed our logos for the company. Borrowdale equity is an investment firm for high level clients looking for advisory in their investments. White background or black is good. We will like to double sided options maybe at the back with just the logo of the firm.

Example of the info for the business card:

Marcus Heller
Managing Director

Panama Phone +507 391 4786
Switzerland Phone +41 43 917 2648
test@borrowdale-equity-example.com
www.borrowdale-equity-example.com

Industry/Entity Type

Investment

```html
<!DOCTYPE html>
<html lang="en">
<head>
<meta charset="utf-8">
<title>Borrowdale Equity Business Card</title>
<link href="https://fonts.googleapis.com/css2?family=Open+Sans:wght@400;600;700&display=swap" rel="stylesheet">
<style>
  :root {
    --backdrop: #ececec;
    --card: #ffffff;
    --navy: #1f3a86;
    --name-blue: #2d6cb4;
    --ink: #1d1d1d;
    --muted: #555555;
  }
  * { box-sizing: border-box; margin: 0; padding: 0; }
  html, body { width: 1200px; height: 1001px; overflow: hidden; }
  body {
    background: var(--backdrop);
    font-family: "Open Sans", sans-serif;
    display: flex;
    align-items: center;
    justify-content: center;
    gap: 60px;
  }
  .card {
    position: relative;
    width: 500px;
    height: 286px;
    background: var(--card);
    box-shadow: 0 6px 18px rgba(0,0,0,0.12);
    overflow: hidden;
  }
  .card__stripe {
    position: absolute;
    left: 0; right: 0; bottom: 0;
    height: 8px;
    background: var(--navy);
  }
  .holder { position: absolute; left: 34px; top: 28px; }
  .holder__name { color: var(--name-blue); font-weight: 700; font-size: 15px; }
  .holder__role { color: var(--muted); font-size: 9px; margin-top: 1px; }
  .contacts {
    position: absolute;
    left: 34px; top: 104px;
    list-style: none;
    font-size: 14px;
    line-height: 19px;
    color: var(--ink);
  }
  .contacts li { display: flex; align-items: center; gap: 10px; }
  .contacts .icon { width: 13px; height: 13px; flex: none; }
  .contacts .icon--blank { visibility: hidden; }
  .wordmark {
    position: absolute;
    display: flex;
    align-items: center;
    gap: 8px;
    color: var(--navy);
    font-weight: 600;
    text-transform: uppercase;
    letter-spacing: 1px;
  }
  .wordmark__square { background: var(--navy); flex: none; }
  .card--front .wordmark { right: 30px; bottom: 40px; font-size: 19px; }
  .card--front .wordmark__square { width: 14px; height: 14px; }
  .card--back .wordmark {
    left: 50%; top: 44%;
    transform: translate(-50%, -50%);
    font-size: 28px;
    white-space: nowrap;
  }
  .card--back .wordmark__square { width: 22px; height: 22px; }
</style>
</head>
<body>
  <section class="card card--front">
    <div class="holder">
      <p class="holder__name">Marcus Heller</p>
      <p class="holder__role">Managing Director</p>
    </div>
    <ul class="contacts">
      <li>
        <svg class="icon" viewBox="0 0 16 16" fill="var(--name-blue)"><path d="M3 2l3 0 1 3-2 1.5c.8 1.8 2.2 3.2 4 4L10.5 8.5l3 1v3c0 .8-.7 1.5-1.5 1.5C6.5 14 2 9.5 2 4c0-.8.2-2 1-2z"/></svg>
        <span>Panama: +507 391 4786</span>
      </li>
      <li>
        <svg class="icon icon--blank" viewBox="0 0 16 16"></svg>
        <span>Switzerland: +41 43 917 2648</span>
      </li>
      <li>
        <svg class="icon" viewBox="0 0 16 16" fill="var(--name-blue)"><path d="M1 3h14v10H1z"/><path d="M1 3l7 6 7-6" fill="none" stroke="#fff" stroke-width="1.3"/></svg>
        <span>test@borrowdale-equity-example.com</span>
      </li>
      <li>
        <svg class="icon" viewBox="0 0 16 16" fill="none" stroke="var(--name-blue)" stroke-width="1.5"><circle cx="8" cy="8" r="6.5" fill="var(--name-blue)"/><ellipse cx="8" cy="8" rx="2.8" ry="6.5" stroke="#fff" stroke-width="1"/><path d="M1.5 8h13" stroke="#fff" stroke-width="1"/></svg>
        <span>www.borrowdale-equity-example.com</span>
      </li>
    </ul>
    <div class="wordmark"><span class="wordmark__square"></span><span>Borrowdale Equity</span></div>
    <div class="card__stripe"></div>
  </section>

  <section class="card card--back">
    <div class="wordmark"><span class="wordmark__square"></span><span>Borrowdale Equity</span></div>
    <div class="card__stripe"></div>
  </section>
</body>
</html>
```